Baufirma sucht Design für Schafkopfkarten
Zielgruppe
Wir sind eine Baufirma und suchen ein schlichtes Design für unsere Schafkopfkarten. Unsere Zielgruppe ist bunt gemischt
Aufgabenstellung
Wir suchen nach einem Design für Schafkopfkarten/Spielkarten.
- Kartenformat 56 x 100 mm
- weißer Rand
- Schlicht
- eventuell Retro Design
- Firmenlogo soll nicht verändert werden
- eventuell 'seit 1946' integrieren

```html
<!DOCTYPE html>
<html lang="de">
<head>
<meta charset="utf-8">
<title>Varlheim Spielkarten – Rückseite</title>
<link href="https://fonts.googleapis.com/css2?family=Rubik:wght@400;600;700&display=swap" rel="stylesheet">
<style>
  :root {
    --page-bg: #ffffff;
    --card-edge: #ffffff;
    --frame-line: #c3c9c7;
    --panel: #50565d;
    --ink: #ffffff;
  }
  html, body {
    margin: 0;
    padding: 0;
    width: 686px;
    height: 1200px;
    overflow: hidden;
    background: var(--page-bg);
  }
  .sheet {
    position: relative;
    width: 686px;
    height: 1200px;
  }
  .card {
    position: absolute;
    top: 399px;
    width: 225px;
    height: 402px;
    background: var(--card-edge);
    box-shadow: 0 6px 22px rgba(0, 0, 0, 0.18);
    font-family: "Rubik", sans-serif;
    color: var(--ink);
  }
  .card--square { left: 96px; }
  .card--rounded { left: 365px; border-radius: 16px; }
  .card__frame {
    position: absolute;
    inset: 8px;
    border: 3px solid var(--frame-line);
    border-radius: 7px;
    background: var(--panel);
  }
  .card__half {
    position: absolute;
    left: 0;
    width: 225px;
    height: 201px;
    top: 0;
  }
  .card__half--flipped {
    top: 201px;
    transform: rotate(180deg);
  }
  .brand-name {
    position: absolute;
    left: 0;
    right: 0;
    top: 96px;
    text-align: center;
    font-weight: 600;
    font-size: 18px;
    letter-spacing: 1.2px;
    line-height: 1;
  }
  .tagline {
    position: absolute;
    left: 0;
    right: 0;
    top: 119px;
    text-align: center;
    font-weight: 400;
    font-size: 6.6px;
    letter-spacing: 0.5px;
    line-height: 1;
    white-space: nowrap;
  }
  .since {
    position: absolute;
    left: 0;
    right: 0;
    top: 146px;
    text-align: center;
    font-weight: 700;
    font-size: 8px;
    letter-spacing: 0.8px;
    line-height: 1;
  }
  .divider {
    position: absolute;
    left: 0;
    top: 193px;
    width: 225px;
    height: 16px;
  }
</style>
</head>
<body>
<div class="sheet">

  <div class="card card--square">
    <div class="card__frame"></div>
    <div class="card__half">
      <div class="brand-name">VARLHEIM</div>
      <div class="tagline">TIEFBAU // ABBRUCH // RECYCLING</div>
      <div class="since">SEIT 1946</div>
    </div>
    <div class="card__half card__half--flipped">
      <div class="brand-name">VARLHEIM</div>
      <div class="tagline">TIEFBAU // ABBRUCH // RECYCLING</div>
      <div class="since">SEIT 1946</div>
    </div>
    <svg class="divider" viewBox="0 0 225 16" aria-hidden="true">
      <line x1="32" y1="8" x2="100" y2="8" stroke="#ffffff" stroke-width="1.5"/>
      <line x1="125" y1="8" x2="193" y2="8" stroke="#ffffff" stroke-width="1.5"/>
      <circle cx="112.5" cy="8" r="6" fill="#ffffff"/>
    </svg>
  </div>

  <div class="card card--rounded">
    <div class="card__frame"></div>
    <div class="card__half">
      <div class="brand-name">VARLHEIM</div>
      <div class="tagline">TIEFBAU // ABBRUCH // RECYCLING</div>
      <div class="since">SEIT 1946</div>
    </div>
    <div class="card__half card__half--flipped">
      <div class="brand-name">VARLHEIM</div>
      <div class="tagline">TIEFBAU // ABBRUCH // RECYCLING</div>
      <div class="since">SEIT 1946</div>
    </div>
    <svg class="divider" viewBox="0 0 225 16" aria-hidden="true">
      <line x1="32" y1="8" x2="100" y2="8" stroke="#ffffff" stroke-width="1.5"/>
      <line x1="125" y1="8" x2="193" y2="8" stroke="#ffffff" stroke-width="1.5"/>
      <circle cx="112.5" cy="8" r="6" fill="#ffffff"/>
    </svg>
  </div>

</div>
</body>
</html>
```